Health/Nutrition/Fitness Graphic needed urgently!

I am looking for a graphic that introduces the concept of health, nutrition and exercise working together to create optimum performance. It needs to exude energy and be clear. It is for a new business called "Vortal" that combines healthcare, nutrition services and fitness training to give clients the best success they can get and will be used in pitch documents, advertising and on the website. The example attached is linear - the winning graphic will need to show each element working together so please do not submit linear graphics. This is NOT a logo, but is a graphic illustrating a concept

Target Market(s)

Clients looking for a transformation in their health and fitness

Industry/Entity Type

Health And Wellness

Font styles to use
Sans Serif

Requirements
Must have
• the 3 elements of health, nutrition and excercise/fitness working together. modern, energetic and clean. What is crucial to show is that these elements work together to leverage effort and enhance/ maximise results.
Should not have
• This is NOT a logo for Vortal and there should be no text in the graphic unless (Health, Fitness and Nutrition are the words used). This is a graphic design used to illustrate a concept only.

```html
<!DOCTYPE html>
<html lang="en">
<head>
<meta charset="utf-8">
<title>Health · Nutrition · Fitness</title>
<link rel="stylesheet" href="https://fonts.googleapis.com/css2?family=Archivo+Black&display=swap">
<style>
  :root {
    --bg: #120406;
    --bg-edge: #070102;
    --inner: #1b0709;
    --health: #e3142a;
    --nutrition: #55b51c;
    --nutrition-dark: #1f4a0a;
    --fitness: #1fb59e;
    --glow: #7a2fc0;
  }
  html, body {
    margin: 0;
    padding: 0;
    width: 1200px;
    height: 675px;
    overflow: hidden;
    background: var(--bg-edge);
  }
  .concept {
    position: relative;
    width: 1200px;
    height: 675px;
    background: radial-gradient(ellipse at 50% 50%, var(--bg) 0%, var(--bg-edge) 85%);
  }
  .concept svg { display: block; width: 1200px; height: 675px; }
  .label {
    font-family: "Archivo Black", "Arial Black", sans-serif;
    font-size: 74px;
  }
</style>
</head>
<body>
<main class="concept">
  <svg viewBox="0 0 1280 720" role="img" aria-label="Health, Nutrition and Fitness triangles locked together">
    <defs>
      <filter id="drop" x="-20%" y="-20%" width="140%" height="140%">
        <feDropShadow dx="4" dy="6" stdDeviation="6" flood-color="#000" flood-opacity="0.7"/>
      </filter>
      <radialGradient id="emblem-health" cx="50%" cy="50%" r="50%">
        <stop offset="0%" stop-color="var(--glow)" stop-opacity="0.55"/>
        <stop offset="60%" stop-color="#1f5f8a" stop-opacity="0.35"/>
        <stop offset="100%" stop-color="var(--inner)" stop-opacity="0"/>
      </radialGradient>
      <radialGradient id="emblem-nutrition" cx="50%" cy="50%" r="50%">
        <stop offset="0%" stop-color="var(--glow)" stop-opacity="0.55"/>
        <stop offset="60%" stop-color="#8a1424" stop-opacity="0.35"/>
        <stop offset="100%" stop-color="var(--inner)" stop-opacity="0"/>
      </radialGradient>
      <radialGradient id="emblem-fitness" cx="50%" cy="50%" r="50%">
        <stop offset="0%" stop-color="var(--glow)" stop-opacity="0.55"/>
        <stop offset="60%" stop-color="#3a7a14" stop-opacity="0.35"/>
        <stop offset="100%" stop-color="var(--inner)" stop-opacity="0"/>
      </radialGradient>
    </defs>

    <!-- colour bands -->
    <rect class="band band-nutrition" x="473" y="0" width="337" height="198" fill="var(--nutrition)"/>
    <rect class="band band-health" x="296" y="574" width="336" height="146" fill="var(--health)"/>
    <rect class="band band-link" x="632" y="498" width="18" height="222" fill="var(--nutrition)"/>
    <rect class="band band-fitness" x="650" y="574" width="338" height="146" fill="var(--fitness)"/>

    <!-- words -->
    <text class="label label-nutrition" x="475" y="194" textLength="332" lengthAdjust="spacingAndGlyphs" fill="var(--nutrition-dark)">NUTRITION</text>
    <text class="label label-health" x="298" y="574" textLength="332" lengthAdjust="spacingAndGlyphs" fill="var(--health)" filter="url(#drop)">HEALTH</text>
    <text class="label label-fitness" x="652" y="574" textLength="334" lengthAdjust="spacingAndGlyphs" fill="var(--fitness)" filter="url(#drop)">FITNESS</text>

    <!-- triangles -->
    <g class="triangle triangle-health" filter="url(#drop)">
      <polygon points="467,200 290,500 642,500" fill="var(--health)"/>
      <polygon points="467,238 320,484 613,484" fill="var(--inner)"/>
    </g>
    <g class="triangle triangle-fitness" filter="url(#drop)">
      <polygon points="818,202 644,500 996,500" fill="var(--fitness)"/>
      <polygon points="818,240 674,484 966,484" fill="var(--inner)"/>
    </g>
    <g class="triangle triangle-nutrition" filter="url(#drop)">
      <polygon points="468,195 816,195 643,497" fill="var(--nutrition)"/>
      <polygon points="498,212 786,212 643,460" fill="var(--inner)"/>
    </g>

    <!-- emblem areas -->
    <g class="emblem emblem-health" role="img" aria-label="Health emblem: glowing medical symbol above a curved accent">
      <ellipse cx="465" cy="372" rx="78" ry="52" fill="url(#emblem-health)"/>
    </g>
    <g class="emblem emblem-nutrition" role="img" aria-label="Nutrition emblem: glowing fruit symbol above a curved accent">
      <ellipse cx="642" cy="292" rx="78" ry="52" fill="url(#emblem-nutrition)"/>
    </g>
    <g class="emblem emblem-fitness" role="img" aria-label="Fitness emblem: glowing strength symbol above a curved accent">
      <ellipse cx="820" cy="372" rx="78" ry="52" fill="url(#emblem-fitness)"/>
    </g>
  </svg>
</main>
</body>
</html>
```